Green Energy Conservation Business Cards

We believe in Conserve before you produce energy. I am looking for a unique, bold business card. that Demonstrates Expertise in our field. I would be interested to try and incorporate a night picture of the US or world showing the yellow lights on one side. I would be open to a design that caters to half the business card size height and same length. Our primary expertise is Energy projects for self storage. Use either black or white background .Attached are the logos and symbols.

May I see some design utilizing a smaller business card. the same length as a normal business card but cut in half on the height. best regards Garrick

```html
<!DOCTYPE html>
<html lang="en">
<head>
<meta charset="utf-8">
<title>Corvel Energy Group – Business Cards</title>
<link href="https://fonts.googleapis.com/css2?family=Arimo:wght@400;700&display=swap" rel="stylesheet">
<style>
  :root {
    --backdrop: #ebebeb;
    --card-white: #ffffff;
    --band-black: #0d0b0a;
    --leaf-green: #7dc242;
    --brand-blue: #1f6fc0;
    --text-white: #f2f2f2;
    --shadow: rgba(0, 0, 0, 0.12);
  }
  * { box-sizing: border-box; margin: 0; padding: 0; }
  html, body {
    width: 1200px;
    height: 972px;
    overflow: hidden;
    background: var(--backdrop);
    font-family: "Arimo", Arial, sans-serif;
  }
  .sheet {
    position: relative;
    width: 1200px;
    height: 972px;
    display: flex;
    align-items: center;
    justify-content: center;
    gap: 60px;
  }
  .card {
    position: relative;
    width: 520px;
    height: 300px;
    background: var(--card-white);
    box-shadow: 0 6px 18px var(--shadow);
  }
  .card__band {
    position: absolute;
    top: 0;
    bottom: 0;
    left: 110px;
    width: 300px;
    background: var(--band-black);
  }

  /* Front */
  .front-mark {
    position: absolute;
    inset: 0;
    display: flex;
    flex-direction: column;
    align-items: center;
    justify-content: center;
    gap: 18px;
  }
  .front-mark__dot {
    width: 110px;
    height: 110px;
    border-radius: 50%;
    background: var(--leaf-green);
  }
  .front-mark__name {
    color: var(--brand-blue);
    font-weight: 700;
    font-size: 22px;
    letter-spacing: 0.5px;
  }

  /* Back */
  .back-content {
    position: absolute;
    inset: 0;
    padding: 34px 22px 0 26px;
    color: var(--text-white);
  }
  .brand {
    display: flex;
    align-items: center;
    gap: 10px;
  }
  .brand__dot {
    width: 38px;
    height: 38px;
    border-radius: 50%;
    background: var(--leaf-green);
    flex-shrink: 0;
  }
  .brand__name {
    color: var(--brand-blue);
    font-weight: 700;
    font-size: 21px;
    line-height: 1.1;
  }
  .person {
    margin-top: 30px;
    font-size: 14px;
    font-weight: 700;
  }
  .person__name { color: var(--leaf-green); }
  .person__divider { color: var(--text-white); font-weight: 400; margin: 0 3px; }
  .person__title { color: var(--brand-blue); font-weight: 400; }
  .contacts {
    list-style: none;
    margin-top: 12px;
    font-size: 12.5px;
    line-height: 1.35;
  }
  .contacts__item {
    display: flex;
    align-items: flex-start;
    gap: 8px;
    margin-bottom: 9px;
  }
  .contacts__icon {
    width: 13px;
    height: 13px;
    flex-shrink: 0;
    margin-top: 2px;
  }
</style>
</head>
<body>
<main class="sheet">

  <section class="card card--front" aria-label="Card front">
    <div class="card__band">
      <div class="front-mark">
        <span class="front-mark__dot"></span>
        <span class="front-mark__name">Corvel Energy Group</span>
      </div>
    </div>
  </section>

  <section class="card card--back" aria-label="Card back">
    <div class="card__band">
      <div class="back-content">
        <div class="brand">
          <span class="brand__dot"></span>
          <span class="brand__name">Corvel Energy Group</span>
        </div>

        <p class="person">
          <span class="person__name">Garrick Holloway</span><span class="person__divider">|</span><span class="person__title">President</span>
        </p>

        <ul class="contacts">
          <li class="contacts__item">
            <svg class="contacts__icon" viewBox="0 0 16 16" aria-hidden="true">
              <circle cx="8" cy="8" r="8" fill="#f2f2f2"/>
              <path d="M8 3.5a3 3 0 0 0-3 3c0 2.2 3 5.8 3 5.8s3-3.6 3-5.8a3 3 0 0 0-3-3z" fill="#0d0b0a"/>
              <circle cx="8" cy="6.5" r="1.1" fill="#f2f2f2"/>
            </svg>
            <span>27 W Maple St<br>Riverton CA 95402</span>
          </li>
          <li class="contacts__item">
            <svg class="contacts__icon" viewBox="0 0 16 16" aria-hidden="true">
              <circle cx="8" cy="8" r="8" fill="#f2f2f2"/>
              <path d="M5.3 4.2l1.4-.3.9 2-.9.8a5.5 5.5 0 0 0 2.6 2.6l.8-.9 2 .9-.3 1.4c-3.6.4-6.9-2.9-6.5-6.5z" fill="#0d0b0a"/>
            </svg>
            <span>(555)014-2280</span>
          </li>
          <li class="contacts__item">
            <svg class="contacts__icon" viewBox="0 0 16 16" aria-hidden="true">
              <circle cx="8" cy="8" r="8" fill="#f2f2f2"/>
              <rect x="4" y="5.2" width="8" height="5.6" fill="none" stroke="#0d0b0a" stroke-width="1.1"/>
              <path d="M4 5.4l4 3 4-3" fill="none" stroke="#0d0b0a" stroke-width="1.1"/>
            </svg>
            <span>garrick@corvelenergy.com</span>
          </li>
        </ul>
      </div>
    </div>
  </section>

</main>
</body>
</html>
```